2 x Digitize Logo | 2 x Business Cards | 2 x Fridge Magnets

We require 6 deliverables:
1. Residential logo redrawn (same just high quality for large print format).
2. Corporate logo redrawn (minor changes to wording and high quality for large print format).
3. New business card design for Furniture Removals (residential)
4. New business card design for Corporate Relocations (business)
5. New Fridge magnet for Furniture removals (residential)
6. New fridge magnet for Corporate Relocations (business)
1. Residential Logo
a. We require the logo to be translated into a high quality digital image with no modifications.
2. Residential Logo
a. We require the logo to be edited (add the word corporate relocations) be translated into a high quality digital image.
3. Using the resilogo please make a new business card for our business.
a. Please see the web site https://www.brightlanehaulage.com.au for colours and inspiration.
b. The residential business card needs the following information:
i. Business Name (using the residential logo).
ii. Free Call: 1800 BL Haul (the Q, P and Move much be the same colour as the logo).
iii. Website: www.BrightLaneHaulage.com.au
iv. Address: 4/7 Ashgrove Court, VIC 3521
v. Email: move@BrightLaneHaulage.com.au
vi. backof Card:
Review our service
www.RateYourStay.com.au
Services: Local, Country, Interstate | Furniture Removals | Piano, Billiard Tables & Antiques
4. Using the corplogo please make a new business card for our business.
b. The corporate business card needs the following information:
i. Business Name (using the corporate logo).
v. Email: corporate@BrightLaneHaulage.com.au
vi. Back of Card:
Review our service
www.RateYourStay.com.au
Services: Corporate relocations | Office equipment moves | Packing Service | Packing Materials
5. Using the resilogo please make a new fridge magent for our business.
b. The residential fidge magnet needs the following information:
iv. Services: Local, Country, Interstate | Furniture Removals | Piano, Billiard Tables & Antiques
6. Using the corplogo please make a new fridge magent for our business.
b. The corporate fidge magnet needs the following information:
iv. Services: Local, Country, Interstate | Corporate relocations
Target Market(s)
Residential Furniture Removals and Corporate Office relocations
Industry/Entity Type
Business
Contact Information for Business Card
Please see full brief for six items required
Requirements
Must have
- Clean simple, easy to read
Nice to have
- fresh, stand out, eye catching
Should not have
- plain, standard, boring, general

```html
<!DOCTYPE html>
<html lang="en">
<head>
<meta charset="utf-8">
<title>Bright Lane Haulage – Corporate Business Card</title>
<link rel="stylesheet" href="https://fonts.googleapis.com/css2?family=Archivo+Black&family=Arimo:wght@400;700&display=swap">
<style>
  :root {
    --backdrop: #ababab;
    --shadow: #595959;
    --card: #ffffff;
    --ink: #000000;
    --brand-red: #c00d0d;
    --brand-green: #0a7a3a;
    --accent-yellow: #f7c200;
    --accent-red: #e8202a;
    --accent-green: #22b14c;
  }
  * { margin: 0; padding: 0; box-sizing: border-box; }
  html, body {
    width: 1200px;
    height: 800px;
    overflow: hidden;
    background: var(--backdrop);
  }
  .canvas {
    position: relative;
    width: 1200px;
    height: 800px;
  }
  .card {
    position: absolute;
    width: 480px;
    height: 320px;
    background: var(--card);
    box-shadow: 19px 17px 0 var(--shadow);
    text-align: center;
    color: var(--ink);
  }
  .card--front { left: 81px; top: 69px; }
  .card--back { left: 618px; top: 398px; }

  .brand {
    position: absolute;
    left: 0; right: 0;
    top: 108px;
    display: flex;
    align-items: center;
    justify-content: center;
    gap: 12px;
  }
  .brand__mark {
    width: 22px; height: 22px;
    border-radius: 50%;
    background: var(--brand-green);
    flex: none;
  }
  .brand__name {
    font-family: "Arimo", Arial, sans-serif;
    font-weight: 700;
    font-size: 21px;
    line-height: 1.2;
    letter-spacing: 0.5px;
    color: var(--brand-red);
    text-align: left;
  }

  .free-call {
    position: absolute;
    left: 0; right: 0;
    top: 202px;
    font-family: "Archivo Black", "Arial Black", sans-serif;
    font-size: 30px;
    line-height: 1;
    letter-spacing: 0.3px;
  }
  .free-call .c-yellow { color: var(--accent-yellow); }
  .free-call .c-red { color: var(--accent-red); }
  .free-call .c-green { color: var(--accent-green); }

  .contact {
    position: absolute;
    left: 0; right: 0;
    top: 235px;
    list-style: none;
    font-family: "Arimo", Arial, sans-serif;
    font-size: 19px;
    line-height: 22.5px;
  }

  .review {
    position: absolute;
    left: 0; right: 0;
    top: 34px;
  }
  .review__title {
    font-family: "Archivo Black", "Arial Black", sans-serif;
    font-size: 37px;
    line-height: 1;
    letter-spacing: 0.5px;
  }
  .review__url {
    font-family: "Archivo Black", "Arial Black", sans-serif;
    font-size: 20px;
    line-height: 1;
    margin-top: 8px;
    margin-left: -8px;
  }

  .services {
    position: absolute;
    left: 20px; right: -14px;
    top: 161px;
    font-family: "Archivo Black", "Arial Black", sans-serif;
    font-size: 20px;
    line-height: 25px;
  }
  .services__label {
    font-family: "Arimo", Arial, sans-serif;
    font-weight: 400;
    color: var(--ink);
    margin-right: 10px;
  }
  .services .c-yellow { color: var(--accent-yellow); }
  .services .c-red { color: var(--accent-red); }
  .services .c-green { color: var(--accent-green); }
</style>
</head>
<body>
<main class="canvas">
  <section class="card card--front" aria-label="Card front">
    <div class="brand">
      <span class="brand__mark"></span>
      <span class="brand__name">BRIGHT LANE HAULAGE<br>CORPORATE RELOCATIONS</span>
    </div>
    <p class="free-call">Free Call: 1800 <span class="c-yellow">B</span><span class="c-red">L</span> <span class="c-green">Haul</span></p>
    <ul class="contact">
      <li>Website: www.BrightLaneHaulage.com.au</li>
      <li>Address: 4/7 Ashgrove Court, VIC 3521</li>
      <li>Email: move@BrightLaneHaulage.com.au</li>
    </ul>
  </section>

  <section class="card card--back" aria-label="Card back">
    <div class="review">
      <h2 class="review__title">Review our service</h2>
      <p class="review__url">www.RateYourStay.com.au</p>
    </div>
    <p class="services">
      <span class="services__label">Services:</span>
      <span class="c-yellow">Corporate relocations</span>
      <span class="c-green">| Office</span>
      <span class="c-red">equipment moves |</span>
      <span class="c-yellow">Packing Service |</span>
      <span class="c-green">Packing Materials</span>
    </p>
  </section>
</main>
</body>
</html>
```